Hire OKRIM

We are developing a website that allows Hospitality employees to apply for hospitality jobs in the OKRIM union. They do this by completing a standarized application form.

The wirefram lays out all of the pages and how they are conected.

The focus is on functinality, simplicity and intuitive.

The site will be in Thai and English.

We're looking for a mok up the first page only to evaluate designs. If we're able to find a design that works, we would ask for the all pages of the wireframe to be completed as per the alocated budget.

Thanks to all the designers for the initial landing pagedesign.  We have committed topayment for a finished design of all 11 pages and windows as per our attachedwireframe.  We would like to choosea final designer by Monday the 7th.x

Reason: We have committed to payment for a finished design of all 11 pages and windows as per our attached wireframe. We would like to choose a final designer by Monday the 7th.

Target Market(s)

Thai nationals ages 20-30 that work in the hospitality industry.

Industry/Entity Type

Hospitality

Colors

Designer to choose colors to be used in the design.

Requirements
Must have
• Intuitive layout
Simple and clean - no redundancy.

```html
<!DOCTYPE html>
<html lang="en">
<head>
<meta charset="utf-8">
<title>Hire OKRIM – Apply</title>
<link href="https://fonts.googleapis.com/css2?family=Cabin:wght@400;600;700&display=swap" rel="stylesheet">
<style>
  :root {
    --brand: #5b95ff;
    --white: #ffffff;
    --ink: #333333;
    --muted: #666666;
    --line: #d9d9d9;
  }
  * { margin: 0; padding: 0; box-sizing: border-box; }
  html, body { width: 1000px; height: 1200px; overflow: hidden; background: var(--white); }
  body { position: relative; font-family: "Cabin", sans-serif; color: var(--ink); }

  .site-header { position: absolute; top: 0; left: 0; width: 1000px; height: 58px; border-bottom: 1px solid var(--line); }
  .brand { position: absolute; left: 42px; top: 0; display: flex; align-items: flex-end; height: 52px; }
  .brand-square { width: 44px; height: 52px; background: var(--brand); }
  .brand-name { margin-left: 9px; font-size: 20px; letter-spacing: 4px; line-height: 1; padding-bottom: 5px; color: var(--ink); }
  .language-switch { position: absolute; left: 466px; top: 21px; display: flex; gap: 9px; }
  .language-switch svg { display: block; }
  .nav-contacts { position: absolute; left: 752px; top: 20px; font-size: 14px; letter-spacing: 4px; color: var(--brand); }
  .nav-login { position: absolute; left: 858px; top: 13px; width: 70px; height: 29px; background: var(--brand); color: var(--white); font-size: 14px; letter-spacing: 3px; display: flex; align-items: center; justify-content: center; }
  .nav-social { position: absolute; left: 946px; top: 22px; font-size: 11px; font-weight: 600; color: var(--brand); }

  .hero { position: absolute; top: 58px; left: 0; width: 1000px; height: 177px; background: var(--brand); color: var(--white); text-align: center; }
  .hero-title { position: absolute; top: 50px; width: 100%; font-size: 25px; font-weight: 400; letter-spacing: 8px; }
  .hero-sub { position: absolute; top: 112px; width: 100%; font-size: 14px; letter-spacing: 4px; }

  .role-tab { position: absolute; top: 278px; width: 114px; height: 39px; font-size: 13px; letter-spacing: 4px; display: flex; align-items: center; justify-content: center; }
  .role-tab--company { left: 366px; border: 1.5px solid var(--brand); color: var(--brand); }
  .role-tab--citizen { left: 519px; background: var(--brand); color: var(--white); }

  .field-label { position: absolute; font-size: 13px; letter-spacing: 4px; color: var(--brand); }
  .field-label--name { left: 194px; top: 438px; }
  .field-label--job { left: 557px; top: 437px; font-weight: 700; font-size: 14px; }
  .field-label--email { left: 194px; top: 499px; }
  .text-input { position: absolute; left: 291px; top: 430px; width: 149px; height: 33px; background: var(--brand); color: var(--white); font-size: 14px; letter-spacing: 3px; padding-left: 13px; display: flex; align-items: center; }
  .caret { display: inline-block; width: 1px; height: 19px; background: var(--white); margin-left: 2px; }
  .select-input { position: absolute; left: 673px; top: 430px; width: 170px; height: 33px; background: var(--brand); color: var(--white); font-size: 14px; letter-spacing: 3px; display: flex; align-items: center; padding-left: 9px; }
  .select-arrow { position: absolute; left: 137px; top: 0; width: 33px; height: 33px; border-left: 1px solid var(--white); display: flex; align-items: center; justify-content: center; }
  .email-placeholder { position: absolute; left: 301px; top: 498px; font-size: 14px; letter-spacing: 3px; color: var(--muted); }
  .submit-button { position: absolute; left: 416px; top: 615px; width: 168px; height: 36px; background: var(--brand); color: var(--white); font-size: 13px; letter-spacing: 3px; display: flex; align-items: center; justify-content: center; }

  .info-band { position: absolute; top: 684px; left: 0; width: 1000px; height: 326px; background: var(--brand); color: var(--white); text-align: center; }
  .info-title { position: absolute; top: 32px; width: 100%; font-size: 23px; font-weight: 400; letter-spacing: 8px; }
  .info-text { position: absolute; top: 72px; width: 100%; font-size: 10.5px; font-weight: 700; letter-spacing: 2.6px; line-height: 13px; }

  .site-footer { position: absolute; top: 1069px; width: 100%; text-align: center; font-size: 13px; font-weight: 700; letter-spacing: 4px; color: var(--ink); padding-left: 14px; }
</style>
</head>
<body>
  <header class="site-header">
    <div class="brand"><span class="brand-square"></span><span class="brand-name">hireokrim</span></div>
    <div class="language-switch">
      <svg width="30" height="19" viewBox="0 0 30 19" role="img" aria-label="Thai language">
        <rect x="0.5" y="0.5" width="29" height="18" fill="#fff" stroke="#222"/>
        <rect x="1" y="1" width="28" height="3" fill="#c8102e"/>
        <rect x="1" y="7" width="28" height="5" fill="#2d2a6e"/>
        <rect x="1" y="15" width="28" height="3" fill="#c8102e"/>
      </svg>
      <svg width="32" height="19" viewBox="0 0 32 19" role="img" aria-label="English language">
        <rect x="0.5" y="0.5" width="31" height="18" fill="#1f2a6b" stroke="#222"/>
        <path d="M1 1 L31 18 M31 1 L1 18" stroke="#fff" stroke-width="4"/>
        <path d="M1 1 L31 18 M31 1 L1 18" stroke="#c8102e" stroke-width="1.4"/>
        <path d="M16 1 V18 M1 9.5 H31" stroke="#fff" stroke-width="6"/>
        <path d="M16 1 V18 M1 9.5 H31" stroke="#c8102e" stroke-width="3"/>
      </svg>
    </div>
    <span class="nav-contacts">contacts</span>
    <span class="nav-login">login</span>
    <span class="nav-social">Socialy</span>
  </header>

  <section class="hero">
    <h1 class="hero-title">WELCOME to HIREOKRIMS</h1>
    <p class="hero-sub">Fill in the form to get started!</p>
  </section>

  <div class="role-tab role-tab--company">company</div>
  <div class="role-tab role-tab--citizen">citezen</div>

  <span class="field-label field-label--name">Name</span>
  <div class="text-input">onFocus<span class="caret"></span></div>
  <span class="field-label field-label--job">job type</span>
  <div class="select-input">receptionist
    <span class="select-arrow"><svg width="12" height="8" viewBox="0 0 12 8"><path d="M0 0 H12 L6 8 Z" fill="#fff"/></svg></span>
  </div>
  <span class="field-label field-label--email">e-mail</span>
  <span class="email-placeholder">your e-mail</span>
  <div class="submit-button">Get me a job!</div>

  <section class="info-band">
    <h2 class="info-title">TITLE</h2>
    <p class="info-text">
      Nulla quis sem at nibh elementum imperdiet. Duis sagittis ipsum. Praesent mauris.<br>
      Fusce nec tellus sed augue semper porta. Mauris massa. Vestibulum lacinia arcu eget nulla.<br>
      Class aptent taciti sociosqu ad litora torquent per conubia nostra, per inceptos himenaeos.<br>
      Curabitur sodales ligula in libero. Sed dignissim lacinia nunc. Curabitur tortor.<br>
      Pellentesque nibh. Aenean quam. In scelerisque sem at dolor. Maecenas mattis.<br>
      Sed convallis tristique sem. Proin ut ligula vel nunc egestas porttitor. Morbi lectus risus,<br>
      iaculis vel, suscipit quis, luctus non, massa. Fusce ac turpis quis ligula lacinia aliquet.<br>
      Mauris ipsum. Nulla metus metus, ullamcorper vel, tincidunt sed, euismod in, nibh.<br>
      Quisque volutpat condimentum velit. Class aptent taciti sociosqu ad litora torquent<br>
      per conubia nostra, per inceptos himenaeos. Nam nec ante. Sed lacinia, urna non tincidunt<br>
      mattis, tortor neque adipiscing diam, a cursus ipsum ante quis turpis. Nulla facilisi.<br>
      Ut fringilla. Suspendisse potenti. Nunc feugiat mi a tellus consequat imperdiet.<br>
      Vestibulum sapien. Proin quam. Etiam ultrices. gna augue eget diam.
    </p>
  </section>

  <footer class="site-footer">FOOTER CONTENT</footer>
</body>
</html>
```